Design the cover for a new all inclusive e-book about crypto currency "Ledger Nine Meridian"

I've written a book for beginners who are curious about crypto currencies in an effort to get them to learn about this new asset class and the opportunities it represents. This book will be for sale on Pellucor so it needs to grab the potential reader's attention. I want it to have a futuristic look and have the title "Ledger Nine Meridian" spelled out in whatever font you think compliments the graphic quality behind it, best. We don't judge a book by it's cover, but on Pellucor we kinda do to get the initial click so someone can read more about it's content. So use your skill set of design to create a really aesthetically pleasing (eye candy if you will) book cover for this literary work and I look forward to speaking with you further if your design gets chosen. If you need some inspiration take a look at some of Rick Varn's book covers.

Target Market(s)

This book will be for people who have never bought or sold digital currency before but are curious about it's opportunity and wealth building characteristics. It was written to be understood by all ages, from the young millennial to your grandma who keeps asking you what that bitcoin stuff is.

Investment

Requirements
Must have
• Author: Gerald Whitby
• Book Title: "Ledger Nine Meridian"
• High attention grabbing graphics or subtlety that still stands out. It's a book cover that will reside in a literal sea of other Pellucor books about similar subject matter. It MUST attract the attention of the curious reader who wants to understand more about this topic, especially if they're already considering investing in it but have no idea where to start. THIS is the book they need to read to learn what they don't know.
Nice to have
• This is digital currency, not tangible assets so maybe think along the lines of movies like The Lattice, Marlinhook, Mask and Lantern where information tends to reside in a dark place in a remote location not readily accessible to most people. Hackers are mentioned in this book as the antagonist to instill fear in the reader so that they take my advice on how to protect their assets which will actually eliminate that fear from the information I provide. You're all designers, I believe you can make an extremely streamlined design with this information.
Should not have
• No effeminate colors like pinks or super crazy neons please. I want this to stand out but it shouldn't look like the sign on a Las Vegas hotel. Lets try and stay away from liberal use of pastels.Nothing feminine looking, it will probably be mostly men that are reading this as my research tends to indicate.

```html
<!DOCTYPE html>
<html lang="en">
<head>
<meta charset="UTF-8">
<title>Ledger Nine Meridian — Gerald Whitby</title>
<link href="https://fonts.googleapis.com/css2?family=Libre+Baskerville:wght@700&display=swap" rel="stylesheet">
<style>
  :root {
    --rack-shadow: #0c2a52;
    --deep-blue: #1a4f8f;
    --mid-blue: #3a7cc2;
    --sky-blue: #8dbbe8;
    --haze: #e3effa;
    --glow: #ffffff;
    --title-ink: #10212f;
    --author-ink: #0a0f16;
  }
  html, body {
    margin: 0;
    padding: 0;
    width: 848px;
    height: 1200px;
    overflow: hidden;
    background: var(--glow);
  }
  .cover {
    position: relative;
    width: 848px;
    height: 1200px;
    overflow: hidden;
  }
  .cover__backdrop {
    position: absolute;
    inset: 0;
    background:
      radial-gradient(ellipse 330px 260px at 42% 86%, var(--glow) 0%, rgba(255,255,255,0.9) 40%, rgba(255,255,255,0) 100%),
      radial-gradient(ellipse 300px 520px at 50% 62%, var(--haze) 0%, rgba(227,239,250,0.7) 45%, rgba(227,239,250,0) 100%),
      radial-gradient(ellipse 260px 160px at 78% 18%, rgba(235,244,252,0.75) 0%, rgba(235,244,252,0) 100%),
      linear-gradient(180deg, rgba(12,42,82,0.25) 0%, rgba(12,42,82,0) 30%, rgba(255,255,255,0) 80%, rgba(210,228,246,0.5) 100%),
      linear-gradient(90deg, var(--rack-shadow) 0%, var(--deep-blue) 10%, var(--mid-blue) 22%, var(--sky-blue) 45%, var(--sky-blue) 68%, var(--mid-blue) 88%, var(--deep-blue) 100%);
  }
  .cover__title {
    position: absolute;
    top: 428px;
    left: 0;
    width: 100%;
    margin: 0;
    text-align: center;
    font-family: "Libre Baskerville", serif;
    font-weight: 700;
    font-size: 100px;
    line-height: 124px;
    letter-spacing: 0;
    color: var(--title-ink);
    text-shadow: 0 0 22px rgba(255,255,255,0.6);
  }
  .cover__title span { display: block; }
  .cover__author {
    position: absolute;
    left: 62px;
    right: 84px;
    top: 1130px;
    margin: 0;
    display: flex;
    justify-content: space-between;
    font-family: "Libre Baskerville", serif;
    font-weight: 700;
    font-size: 32px;
    line-height: 40px;
    color: var(--author-ink);
  }
  .cover__author .gap { width: 48px; }
</style>
</head>
<body>
  <main class="cover">
    <div class="cover__backdrop" role="img" aria-label="Photograph of a glowing blue data-center corridor lined with server racks and blinking lights, ceiling light panels receding toward a bright white haze at the far end"></div>
    <h1 class="cover__title">
      <span>LEDGER</span>
      <span>NINE</span>
      <span>MERIDIAN</span>
    </h1>
    <p class="cover__author" aria-label="Gerald Whitby">
      <span>G</span><span>E</span><span>R</span><span>A</span><span>L</span><span>D</span><span class="gap"></span><span>W</span><span>H</span><span>I</span><span>T</span><span>B</span><span>Y</span>
    </p>
  </main>
</body>
</html>
```